New LGBT Nightclub Crowdfunding Poster

We need it to read well for social media posts. All colors should look similar to Seattle’s Sports Teams color schemes.

The top should have: The logo prominently with the fans in the background photo. and then still center and important, "Coming soon!" "You can be part of the first in line for the amazing things happening". (The call to action is the purchase of these amazing deals for the first weekend open / passes. That should be clear).

```html
<!DOCTYPE html>
<html lang="en">
<head>
<meta charset="utf-8">
<title>The Rally Room — Coming Soon</title>
<link rel="stylesheet" href="https://fonts.googleapis.com/css2?family=Oswald:wght@600&family=Montserrat:wght@700;800&display=swap">
<style>
  :root {
    --page-bg: #e9eaec;
    --ice-light: #f3f7fb;
    --ice-mid: #dbe6f1;
    --ice-deep: #c9d8e8;
    --navy: #0d2a66;
    --navy-band: #0b2866;
    --green: #117a46;
    --green-bright: #14a35c;
    --white: #ffffff;
  }
  * { box-sizing: border-box; margin: 0; padding: 0; }
  html, body {
    width: 1200px; height: 942px; overflow: hidden;
    background: var(--page-bg);
  }
  .poster {
    position: absolute; left: 288px; top: 31px;
    width: 624px; height: 880px; overflow: hidden;
    background:
      radial-gradient(ellipse at 50% 40%, var(--ice-light) 0%, transparent 60%),
      linear-gradient(180deg, var(--ice-mid) 0%, var(--ice-light) 45%, var(--ice-deep) 100%);
    box-shadow: 0 4px 14px rgba(0,0,0,.18);
    text-align: center;
  }
  .crowd-art {
    position: absolute; left: 221px; top: 22px;
    width: 182px; height: 150px;
    border-radius: 48% 52% 46% 54% / 40% 40% 60% 60%;
    background: radial-gradient(circle at 50% 60%, #3f4d7e 0%, #2a3566 60%, #8895b8 100%);
  }
  .brand-name {
    position: absolute; left: 0; right: 0; top: 182px;
    font: 700 20px/1 "Montserrat", sans-serif;
    letter-spacing: 2px; color: var(--navy);
  }
  .headline {
    position: absolute; left: 0; right: 0;
    font-family: "Oswald", sans-serif; font-weight: 600;
    font-size: 172px; line-height: 1;
    text-shadow: 0 0 2px var(--white), 2px 2px 0 var(--white);
  }
  .headline--coming { top: 214px; color: var(--navy); letter-spacing: 1px; }
  .headline--soon { top: 358px; color: var(--green); }
  .intro {
    position: absolute; left: 40px; right: 40px; top: 548px;
    font: 700 30px/41px "Montserrat", sans-serif;
    color: var(--navy);
  }
  .cta-band {
    position: absolute; left: 0; bottom: 0; width: 624px; height: 182px;
  }
  .cta {
    position: absolute; left: 0; right: 0; top: 736px;
    color: var(--white);
  }
  .cta__lead { font: 700 23px/1 "Montserrat", sans-serif; }
  .cta__deals {
    margin-top: 8px;
    font: 800 57px/1 "Montserrat", sans-serif;
    color: var(--green-bright); letter-spacing: -0.5px;
  }
  .cta__detail { margin-top: 8px; font: 700 22px/1 "Montserrat", sans-serif; }
</style>
</head>
<body>
  <main class="poster">
    <div class="crowd-art" role="img" aria-label="Silhouetted crowd of fans with raised arms"></div>
    <div class="brand-name">THE RALLY ROOM</div>

    <h1 class="headline headline--coming">COMING</h1>
    <h1 class="headline headline--soon">SOON</h1>

    <p class="intro">You can be part of the first<br>in line for the amazing<br>things happening</p>

    <svg class="cta-band" viewBox="0 0 624 182" preserveAspectRatio="none" aria-hidden="true">
      <path d="M0 40 Q312 -30 624 40 L624 182 L0 182 Z" fill="var(--green)"/>
      <path d="M0 46 Q312 -18 624 46 L624 182 L0 182 Z" fill="var(--navy-band)"/>
    </svg>
    <div class="cta">
      <p class="cta__lead">PURCHASE OF THESE</p>
      <p class="cta__deals">AMAZING DEALS</p>
      <p class="cta__detail">FOR THE FIRST WEEKEND OPEN / PASSES</p>
    </div>
  </main>
</body>
</html>
```